Business Management System Providor Needs Upscale Business Card Design

We provide an online Claims Management System to the Insurance Industry called Meridell Casework Suite. Although our core offering is claims management, our system provides full business management features including reporting, invoicing, business trend analysis, etc..
We have a worldwide client base and our system has become known for its reliability, rich feature set, and intuitive design. This being the case we would like our cards to maintain a high level of professionalism. We have a tendency to lean toward a corporate look and feel and we would like to maintain that image.
Current Site: www.meridellcaseworksuite.example
Target Market(s)
Big Business, Insurance Professionals, Corporate Organizations
Industry/Entity Type
Business Management
Look and feel
Each slider illustrates characteristics of the customer's brand and the style your logo design should communicate.

```html
<!DOCTYPE html>
<html lang="en">
<head>
<meta charset="utf-8">
<title>Meridell Casework Suite – Business Card</title>
<link rel="stylesheet" href="https://fonts.googleapis.com/css2?family=Fira+Sans:wght@300;400;600&display=swap">
<style>
  :root {
    --page: #ffffff;
    --card-top: #ffffff;
    --card-bottom: #dcdcdc;
    --card-edge: #d2d2d2;
    --brand-navy: #1d3f6e;
    --accent-blue: #1a54a0;
    --text-grey: #4a4a4a;
    --tag-grey: #8a8a8a;
  }
  html, body {
    margin: 0;
    width: 1200px;
    height: 1000px;
    overflow: hidden;
    background: var(--page);
    font-family: "Fira Sans", Arial, sans-serif;
  }
  .canvas { position: relative; width: 1200px; height: 1000px; }
  .card {
    position: absolute;
    left: 131px; top: 187px;
    width: 954px; height: 618px;
    border: 1px solid var(--card-edge);
    border-radius: 40px;
    overflow: hidden;
    box-sizing: border-box;
  }
  .card-surface {
    position: absolute; inset: 0;
    background: linear-gradient(to bottom, var(--card-top) 0%, var(--card-top) 30%, var(--card-bottom) 100%);
  }
  .card-lines { position: absolute; left: 0; top: 0; }
  .brand { position: absolute; left: 72px; top: 72px; }
  .brand-mark {
    position: absolute; left: 0; top: 0;
    width: 88px; height: 88px;
    background: var(--brand-navy);
    border-radius: 8px;
  }
  .brand-name {
    position: absolute; left: 106px; top: 6px;
    margin: 0;
    font-weight: 600; font-size: 27px; line-height: 30px;
    color: var(--brand-navy);
    white-space: nowrap;
  }
  .brand-tagline {
    position: absolute; left: 0; top: 104px;
    margin: 0;
    font-weight: 400; font-size: 19px;
    color: var(--tag-grey);
    white-space: nowrap;
  }
  .office-title {
    position: absolute; right: 130px; top: 200px;
    margin: 0;
    font-weight: 400; font-size: 47px; line-height: 60px;
    color: var(--accent-blue);
  }
  .info {
    position: absolute;
    margin: 0;
    font-weight: 400; font-size: 26px; line-height: 32px;
    color: var(--text-grey);
    white-space: nowrap;
  }
  .info .label { color: var(--accent-blue); }
  .right { text-align: right; }
</style>
</head>
<body>
<div class="canvas">
  <div class="card">
    <div class="card-surface" role="img" aria-label="Soft white-to-grey background with a faint interlocking pattern"></div>

    <svg class="card-lines" width="954" height="618" viewBox="0 0 954 618" aria-hidden="true">
      <line x1="439" y1="261" x2="954" y2="261" stroke="#1a54a0" stroke-width="3"/>
      <circle cx="428" cy="261" r="11" fill="#ffffff" stroke="#1a54a0" stroke-width="3"/>
      <line x1="0" y1="478" x2="584" y2="478" stroke="#1a54a0" stroke-width="3"/>
      <circle cx="595" cy="478" r="11" fill="#ffffff" stroke="#1a54a0" stroke-width="3"/>
    </svg>

    <div class="brand">
      <div class="brand-mark"></div>
      <p class="brand-name">Meridell<br>Casework<br>Suite</p>
      <p class="brand-tagline">claim management systems</p>
    </div>

    <h1 class="office-title">Head Office</h1>

    <p class="info right" style="right:287px; top:298px;">1180 Harrowgate Avenue West</p>
    <p class="info right" style="right:129px; top:298px;">Suite 800</p>
    <p class="info right" style="right:368px; top:344px;">Brantwell, ON,</p>
    <p class="info right" style="right:129px; top:344px;">Canada, L7R 2M9</p>
    <p class="info" style="left:374px; top:395px;"><span class="label">T</span>: 416.555.0142</p>
    <p class="info" style="left:626px; top:395px;"><span class="label">F</span>: 866.555.0198</p>

    <p class="info" style="left:626px; top:463px;">United Kingdom</p>
    <p class="info" style="left:614px; top:511px;"><span class="label">T</span>: 0121.496.0375</p>
  </div>
</div>
</body>
</html>
```